Website Redesign for Asset Management

We need a full redesign on the website for Velbrook Asset Management. Velbrook is an asset manager that manages both long - only products and alternative investments. We would like to see a clean and innovative website that showcases the products of the firm and the management of the firm.
www.velbrook-example.com
Updates

Output should be in PSD and designer should have groups/layers for the developer to extract the imagesĀ 

Feel free to play with the colours as we are not stuck to current colours.

Target Market(s)

The target market are affluent individuals, pensions, foundations and endowments

Industry/Entity Type

Asset Management

Requirements
Must have
• We like the websites
www.dalvertcourt-example.com
www.quillanfunds-example.com
DO LIKE
http://www.morvatek-example.com/#Home
http://www.dalvertcourt-example.com/who-we-are/principals.html
http://www.ktrellin-example.com/default.aspx
http://www.qp4-example.ca/
http://www.parvenholt-example.com/Home
https://www.lumivaleholdings-example.com/index.asp
http://www.crispell-example.ca/Home_Page.html
http://www.dqrmoxley-example.com/#!contact/c16fm
http://www.fenstraleinvest-example.com/
http://www.oberlyn-example.com/
https://www.quessagroup-example.com/
http://www.mkvor-example.com/
http://www.hadrickgroup-example.com/

Don't Like
http://www.silvertallow-example.com
http://kemble-example.com/
http://rvandolin-example.com/
http://www.ptwilder-example.com/operations_team.html

Also must have a section entitles Alternative Investments

```html
<!DOCTYPE html>
<html lang="en">
<head>
<meta charset="utf-8">
<title>Velbrook Asset Management</title>
<link rel="stylesheet" href="https://fonts.googleapis.com/css2?family=Arimo:wght@400;700&family=Oswald:wght@500;600&display=swap">
<style>
  :root {
    --ink: #1a1a1a;
    --gold: #ffcc00;
    --olive: #6b5a10;
    --mustard: #b8900a;
    --card-bg: #efefef;
    --tri-gold: #ffcc00;
    --tri-taupe: #a89080;
    --tri-grey: #9a9a9a;
    --tri-sage: #9ca08a;
    --footer-bg: #2c2c2c;
    --footer-text: #ffffff;
    --dot: #a89a5a;
    --hero-top: #5a3c22;
    --hero-bottom: #5e6a2e;
  }
  * { margin: 0; padding: 0; box-sizing: border-box; }
  html, body { width: 1200px; height: 900px; overflow: hidden; background: #fff; }
  body { position: relative; font-family: "Arimo", Arial, sans-serif; color: var(--ink); }

  .site-header {
    position: absolute; left: 0; top: 0; width: 1200px; height: 100px;
    background: linear-gradient(90deg, #ececec 0%, #fff 8%, #fff 92%, #ececec 100%);
  }
  .brand { position: absolute; left: 121px; top: 38px; font-size: 32px; color: var(--ink); letter-spacing: 0.5px; }
  .main-nav { position: absolute; right: 112px; top: 49px; display: flex; gap: 22px; font-size: 16px; }
  .main-nav a { color: var(--ink); text-decoration: none; }
  .header-rule { position: absolute; left: 111px; top: 95px; width: 979px; height: 4px; background: var(--gold); }

  .hero { position: absolute; left: 0; top: 100px; width: 1200px; height: 340px; overflow: hidden; }
  .hero-photo { position: absolute; inset: 0; background: linear-gradient(180deg, var(--hero-top) 0%, var(--hero-bottom) 100%); }
  .hero-copy { position: absolute; left: 122px; top: 104px; color: #fff; text-shadow: 2px 2px 4px rgba(0,0,0,0.6); }
  .hero-copy .line-sm { font-size: 30px; line-height: 36px; }
  .hero-copy .line-lg { font-size: 43px; line-height: 50px; }
  .hero-copy .line-md { font-size: 28px; line-height: 58px; }
  .slider-dots { position: absolute; left: 926px; top: 309px; display: flex; gap: 9px; }
  .slider-dots span { width: 10px; height: 10px; background: var(--dot); }

  .tagline-band { position: absolute; left: 111px; top: 441px; width: 979px; height: 81px; background: var(--gold); overflow: hidden; }
  .tagline-ghost { position: absolute; left: 16px; top: 17px; font-size: 48px; color: rgba(150,110,0,0.25); white-space: nowrap; }
  .tagline { position: absolute; left: 56px; top: 22px; font-size: 36px; color: var(--olive); white-space: nowrap; }
  .social { position: absolute; right: 28px; top: 28px; display: flex; gap: 11px; }
  .social span { width: 30px; height: 30px; border-radius: 50%; background: #111; border: 2px solid #000; }

  .featured-title { position: absolute; left: 116px; top: 543px; font-size: 30px; font-weight: 400; }
  .fund-list { position: absolute; left: 110px; top: 588px; display: flex; gap: 9px; }
  .fund-card { width: 238px; }
  .fund-head { position: relative; height: 72px; background: var(--card-bg); }
  .fund-head svg { position: absolute; left: 0; top: 0; }
  .fund-code { position: absolute; left: 7px; top: 3px; font-family: "Oswald", "Arial Narrow", sans-serif; font-weight: 600; font-size: 27px; color: #333; }
  .fund-name { position: absolute; right: 12px; top: 18px; text-align: right; color: #222; white-space: nowrap; }
  .fund-name .name { font-size: 18px; line-height: 22px; }
  .fund-name .type { font-size: 15px; line-height: 22px; }
  .fund-desc { margin-top: 7px; text-align: center; font-size: 14px; line-height: 18px; color: #333; white-space: nowrap; }
  .fund-card.gold .fund-desc { margin-top: 5px; }
  .fund-desc .mark { color: var(--mustard); }
  .fund-card.taupe .mark { color: #7a6554; }
  .fund-card.grey .mark { color: #777; }
  .fund-card.sage .mark { color: #5c6046; }

  .site-footer { position: absolute; left: 110px; top: 744px; width: 980px; height: 156px; background: var(--footer-bg); color: var(--footer-text); }
  .site-footer h3 { font-size: 22px; font-weight: 400; line-height: 26px; margin-bottom: 16px; }
  .footer-col { position: absolute; top: 22px; font-size: 13px; line-height: 17px; }
  .sitemap { left: 30px; }
  .sitemap ul { margin-top: -4px; }
  .sitemap li { list-style: none; font-size: 14px; line-height: 17px; }
  .about { left: 234px; width: 373px; text-align: justify; }
  .contact { left: 668px; width: 300px; white-space: nowrap; }
</style>
</head>
<body>
  <header class="site-header">
    <div class="brand">Velbrook</div>
    <nav class="main-nav">
      <a href="#">Home</a><a href="#">Profile</a><a href="#">Investment Process</a>
      <a href="#">investment Solutions</a><a href="#">News &amp; events</a><a href="#">Contact Us</a>
    </nav>
    <div class="header-rule"></div>
  </header>

  <section class="hero">
    <div class="hero-photo" role="img" aria-label="Hero photograph placeholder: autumn countryside landscape"></div>
    <div class="hero-copy">
      <div class="line-sm">Your money will be managed</div>
      <div class="line-lg">right alongside money that is very near</div>
      <div class="line-md">and dear to us. Ours.</div>
    </div>
    <div class="slider-dots"><span></span><span></span><span></span><span></span><span></span><span></span><span></span><span></span></div>
  </section>

  <section class="tagline-band">
    <div class="tagline-ghost" aria-hidden="true">Growing Wealth Preserving Capital</div>
    <div class="tagline">Growing Wealth Preserving Capital</div>
    <div class="social" aria-label="Social links"><span></span><span></span><span></span><span></span></div>
  </section>

  <h2 class="featured-title">Featured Funds</h2>
  <div class="fund-list">
    <article class="fund-card gold">
      <div class="fund-head">
        <svg width="106" height="72"><polygon points="0,0 106,0 0,72" fill="var(--tri-gold)"/></svg>
        <span class="fund-code">QHE</span>
        <div class="fund-name"><div class="name">Quillan Tactical</div><div class="type">HEDGED EQUITY FUND</div></div>
      </div>
      <p class="fund-desc"><span class="mark">MY VELBROOK</span> is to target market<br>returns with substantially less<br>market volatility.</p>
    </article>
    <article class="fund-card taupe">
      <div class="fund-head">
        <svg width="106" height="72"><polygon points="0,0 106,0 0,72" fill="var(--tri-taupe)"/></svg>
        <span class="fund-code">QDF</span>
        <div class="fund-name"><div class="name">Quillan Core</div><div class="type">DIVIDEND FUND</div></div>
      </div>
      <p class="fund-desc"><span class="mark">MY VELBROOK</span> is to grow<br>dividends and distribute them as<br>tax-efficiently as possible</p>
    </article>
    <article class="fund-card grey">
      <div class="fund-head">
        <svg width="106" height="72"><polygon points="0,0 106,0 0,72" fill="var(--tri-grey)"/></svg>
        <span class="fund-code">QBD</span>
        <div class="fund-name"><div class="name">Quillan Total</div><div class="type">RETURN BOND FIND</div></div>
      </div>
      <p class="fund-desc"><span class="mark">MY VELBROOK</span> is to help<br>manage your fixed income<br>better</p>
    </article>
    <article class="fund-card sage">
      <div class="fund-head">
        <svg width="106" height="72"><polygon points="0,0 106,0 0,72" fill="var(--tri-sage)"/></svg>
        <span class="fund-code">QRA</span>
        <div class="fund-name"><div class="name">Quillan Diversifed</div><div class="type">REAL ASSET FUND</div></div>
      </div>
      <p class="fund-desc"><span class="mark">MY VELBROOK</span> is to protect your<br>purchasing power while diversifying<br>your portfolio</p>
    </article>
  </div>

  <footer class="site-footer">
    <div class="footer-col sitemap">
      <h3>Site Map</h3>
      <ul>
        <li>Profile</li><li>Investment Process</li><li>investment Solutions</li>
        <li>Alternative Investments</li><li>News &amp; events</li>
      </ul>
    </div>
    <div class="footer-col about">
      <h3>About Velbrook</h3>
      <p>Velbrook Asset Management Inc. is an independent and focused portfolio management firm servicing high net worth families, foundations and institutions. Balancing growth with capital preservation</p>
    </div>
    <div class="footer-col contact">
      <h3>Contact Us</h3>
      <p>48 Larkin Street West, North Tower 21st Floor<br>P.O. Box 214, Toronto, ON M4Q 2R7,<br>Tel: 416.555.0148, Toll: 877.555.0163<br>Fax: 416.555.0149, Email: Click Here</p>
    </div>
  </footer>
</body>
</html>
```